Hot summer sales event

Looking for a banner/billboard design for my website.

Check out my current website
www.brimwaveautos.ca
We are a car dealership specializing in performance and classic cars.

I would like to highlight these 4 services

BUY, SELL, TRADE, CONSIGN

Target Market(s)

car buyers

Industry/Entity Type

Automotive

Colors
f68e4d
ec1f27
ffc214
fbee3e

Requirements
Must have
• Save thousands
Nice to have
• Pictures of sport cars

```html
<!DOCTYPE html>
<html lang="en">
<head>
<meta charset="utf-8">
<title>Hot Summer Sales Event – Brimwave Autos</title>
<link rel="stylesheet" href="https://fonts.googleapis.com/css2?family=Libre+Baskerville:ital,wght@1,400;1,700&family=Montserrat:wght@400;500;600;800;900&display=swap">
<style>
  :root {
    --page-bg: #eceef1;
    --maroon-deep: #5c0b0b;
    --maroon-dark: #1c0404;
    --gold: #ffc214;
    --gold-soft: #e0a83a;
    --sun-orange: #f68e4d;
    --hot-red: #ec1f27;
    --lemon: #fbee3e;
    --white: #ffffff;
    --ink: #1a1010;
  }
  * { margin: 0; padding: 0; box-sizing: border-box; }
  html, body { width: 1200px; height: 962px; overflow: hidden; background: var(--page-bg); }
  .billboard {
    position: absolute; left: 40px; top: 338px;
    width: 1120px; height: 286px; overflow: hidden;
    background: linear-gradient(90deg, var(--maroon-deep) 0%, #3a0707 45%, var(--maroon-dark) 60%);
    font-family: "Montserrat", sans-serif;
  }
  .eyebrow {
    position: absolute; left: 38px; top: 30px;
    font-family: "Libre Baskerville", serif; font-style: italic; font-weight: 400;
    font-size: 21px; color: var(--gold-soft); text-transform: uppercase; white-space: nowrap;
  }
  .headline {
    position: absolute; left: 38px; top: 66px;
    font-family: "Libre Baskerville", serif; font-style: italic; font-weight: 700;
    font-size: 34px; color: var(--white); text-transform: uppercase; white-space: nowrap;
  }
  .services { position: absolute; left: 42px; top: 143px; display: flex; gap: 28px; }
  .service-group {
    border-left: 3px solid var(--gold-soft); padding-left: 16px;
    display: flex; flex-direction: column; gap: 19px; width: 104px;
  }
  .service-group span {
    font-size: 18px; font-weight: 500; color: var(--white); line-height: 22px;
    letter-spacing: 0.5px; text-transform: uppercase;
  }
  .appointment { position: absolute; left: 40px; top: 236px; font-size: 12.5px; color: var(--white); line-height: 18px; }
  .appointment strong { font-weight: 700; }
  .brand-box {
    position: absolute; left: 452px; top: 0; width: 112px; height: 110px;
    background: var(--white); display: flex; flex-direction: column;
    align-items: center; justify-content: center; gap: 6px;
  }
  .brand-dot { width: 22px; height: 22px; border-radius: 50%; background: var(--gold); }
  .brand-name {
    font-size: 13px; font-weight: 800; color: var(--gold); text-align: center;
    line-height: 14px; text-transform: uppercase;
  }
  .savings {
    position: absolute; left: 352px; top: 126px; transform: rotate(-7deg);
    font-size: 16px; font-weight: 800; color: var(--lemon);
    text-transform: uppercase; letter-spacing: 1px; white-space: nowrap;
  }
  .event-sticker {
    position: absolute; left: 334px; top: 162px; width: 262px; height: 88px;
    transform: rotate(-7deg); background: rgba(20, 8, 8, 0.55);
    border-top: 4px solid var(--gold); border-bottom: 4px solid var(--gold);
    display: flex; flex-direction: column; justify-content: center; padding-left: 8px;
  }
  .event-sticker span { font-weight: 900; font-size: 32px; line-height: 34px; text-transform: uppercase; letter-spacing: -0.5px; white-space: nowrap; }
  .event-hot { color: var(--gold); }
  .event-sales { color: var(--hot-red); padding-left: 4px; }
  .car-photo {
    position: absolute; left: 629px; top: 0; width: 491px; height: 286px;
    background: radial-gradient(ellipse at 45% 45%, var(--lemon) 0%, var(--gold) 40%, #c99a0a 65%, #3a2e22 95%);
  }
</style>
</head>
<body>
  <main class="billboard">
    <p class="eyebrow">Automotive Sale Offer!</p>
    <h1 class="headline">Hot Sale Event</h1>
    <div class="services">
      <div class="service-group"><span>Buy</span><span>Sell</span></div>
      <div class="service-group"><span>Trade</span><span>Consign</span></div>
    </div>
    <p class="appointment">Book Your Appointment Now<br>Please Call <strong>403-555-0142</strong></p>
    <div class="brand-box">
      <div class="brand-dot"></div>
      <div class="brand-name">Brimwave<br>Autos.ca</div>
    </div>
    <p class="savings">Save Thousands!</p>
    <div class="event-sticker">
      <span class="event-hot">Hot Summer</span>
      <span class="event-sales">Sales Event</span>
    </div>
    <div class="car-photo" role="img" aria-label="Photo of a yellow sports car, front corner close-up"></div>
  </main>
</body>
</html>
```